Retro Label for old fashioned soda

We need a label for soda we are having private labeled for our retro, 1950's ice cream shop www.maplewhirlcones.com I don't want the label to look like something from 2017 with a retro feel, but more like an original (possibly kinda cheesy) label you'd see from the 1950's with some of the old catch lines like "tastes great", "invigorating" or "it is refreshing!" The prominent brand should be the name of our ice cream shop, The Maple Whirl. the soda is also pure cane sugar so it might be good to have that on somewhere

Label size is 2.4" wide by 4" tall. Here is an example of some retro labels from findoramap. I attached on file to this contest but there are more here: https://www.findoramap.net/search?q=retro+soda+label

The label will be the same for all the flavors with the exception of the flavor name changing somewhere on the label. These are the flavors

Root Beer
Orange
Black Cherry
Lemonade
Raspberry Lime -Rickey
White Birch Beer
Lemon Iced Tea
Vanilla Cream
Orange Cream
Sarsaparilla
Ginger Ale

Industry/Entity Type

Shop

Colors

Designer to choose colors to be used in the design.

Requirements
Must have
• retro feel. authentic old fashioned look

```html
<!DOCTYPE html>
<html lang="en">
<head>
<meta charset="utf-8">
<title>The Maple Whirl – Sarsaparilla Label</title>
<link rel="stylesheet" href="https://fonts.googleapis.com/css2?family=Alfa+Slab+One&family=Bitter:ital,wght@1,800&display=swap">
<style>
  :root {
    --cream: #fbf3da;
    --brick: #c4574a;
    --ornament: #e6b9a8;
  }
  * { margin: 0; padding: 0; box-sizing: border-box; }
  html, body { width: 721px; height: 1200px; overflow: hidden; background: var(--cream); }
  .label {
    position: relative;
    width: 721px;
    height: 1200px;
    background: var(--cream);
    color: var(--brick);
    overflow: hidden;
  }
  .label-art { position: absolute; inset: 0; }
  .brand-name {
    position: absolute;
    left: 40px; width: 641px; top: 165px;
    text-align: center;
    font-family: "Alfa Slab One", serif;
    font-weight: 400;
    font-size: 92px;
    line-height: 1.08;
    color: var(--brick);
  }
  .brand-line { display: block; }
  .flavor-plate {
    position: absolute;
    left: 42px; top: 566px;
    width: 637px; height: 66px;
    background: var(--cream);
    border: 3px solid var(--brick);
    box-shadow: 0 0 0 3px var(--cream), 0 0 0 5px var(--brick);
    display: flex; align-items: center; justify-content: center;
  }
  .flavor-name {
    font-family: "Alfa Slab One", serif;
    font-size: 58px;
    line-height: 1;
    letter-spacing: 3px;
    color: var(--cream);
    -webkit-text-stroke: 2px var(--brick);
    text-shadow: -3px 3px 0 var(--brick), -5px 5px 0 var(--brick);
  }
  .slogan-banner {
    position: absolute;
    left: 140px; top: 760px;
    width: 441px; height: 200px;
    background: var(--brick);
  }
  .slogan {
    position: absolute;
    left: 0; width: 721px; top: 800px;
    text-align: center;
    font-family: "Bitter", serif;
    font-style: italic;
    font-weight: 800;
    color: var(--cream);
    line-height: 1;
  }
  .slogan-small { display: block; font-size: 58px; }
  .slogan-big { display: block; font-size: 76px; margin-top: -2px; }
  .sugar-band {
    position: absolute;
    left: 14px; top: 1056px;
    width: 693px; height: 104px;
    background: var(--brick);
    display: flex; align-items: center; justify-content: center;
  }
  .sugar-line {
    font-family: "Alfa Slab One", serif;
    font-size: 23px;
    letter-spacing: 4px;
    word-spacing: 10px;
    color: var(--cream);
    white-space: nowrap;
  }
</style>
</head>
<body>
<main class="label">
  <svg class="label-art" width="721" height="1200" viewBox="0 0 721 1200" xmlns="http://www.w3.org/2000/svg">
    <rect class="frame-outer" x="10" y="10" width="701" height="1180" fill="none" stroke="var(--brick)" stroke-width="5"/>
    <rect class="frame-inner" x="22" y="22" width="677" height="1156" fill="none" stroke="var(--brick)" stroke-width="2"/>
    <rect x="42" y="24" width="146" height="115" fill="var(--ornament)" role="img" aria-label="Decorative scrollwork flourish, top left corner"/>
    <rect x="533" y="24" width="146" height="115" fill="var(--ornament)" role="img" aria-label="Decorative scrollwork flourish, top right corner"/>
    <rect x="278" y="392" width="146" height="66" fill="var(--ornament)" role="img" aria-label="Sunburst ornament with scroll curls"/>
    <line x1="210" y1="458" x2="510" y2="458" stroke="var(--brick)" stroke-width="3"/>
    <path d="M22 515 Q360 440 699 515" fill="none" stroke="var(--brick)" stroke-width="3"/>
    <path d="M22 532 Q360 458 699 532" fill="none" stroke="var(--brick)" stroke-width="2"/>
    <path d="M22 572 Q360 490 699 572 L699 665 Q360 590 22 665 Z" fill="var(--brick)"/>
    <path d="M22 688 Q360 614 699 688" fill="none" stroke="var(--brick)" stroke-width="3"/>
    <line x1="14" y1="1040" x2="707" y2="1040" stroke="var(--brick)" stroke-width="3"/>
    <line x1="14" y1="1178" x2="707" y2="1178" stroke="var(--brick)" stroke-width="3"/>
  </svg>

  <h1 class="brand-name"><span class="brand-line">The Maple</span><span class="brand-line">Whirl</span></h1>

  <div class="flavor-plate"><span class="flavor-name">SARSAPARILLA</span></div>

  <div class="slogan-banner" role="img" aria-label="Curled ribbon scroll banner carrying the slogan"></div>
  <p class="slogan"><span class="slogan-small">tastes</span><span class="slogan-big">Great!</span></p>

  <div class="sugar-band"><span class="sugar-line">MADE WITH PURE CANE SUGAR</span></div>
</main>
</body>
</html>
```